Harmonies of the Coast Presents

Show name:
Maple Chorus Revue
Location:
Larkwood High School
4286 Fernhollow Rd, Citrus Heights, CA 95617
Times: 2 p.m. & 7 p.m.
Special Guests:
Bright Chord
Harbor Quartet
Copperleaf Five
Ticket Prices:
VIP $35.00
General $25.00
Student $15.00

```html
<!DOCTYPE html>
<html lang="en">
<head>
<meta charset="UTF-8">
<title>Maple Chorus Revue</title>
<link rel="stylesheet" href="https://fonts.googleapis.com/css2?family=Cormorant+Garamond:wght@500;700&family=Kaushan+Script&family=Archivo:wght@700;800&display=swap">
<style>
  :root {
    --plum-light: #6a1f74;
    --plum-mid: #3f0f4c;
    --plum-deep: #250832;
    --gold: #f7c24a;
    --gold-light: #ffd978;
    --cream: #fdf0cf;
    --white: #ffffff;
    --rule: #a58aa8;
    --sage: #8cbfa3;
    --petal-pink: #f3a9c8;
    --petal-rose: #e2677a;
    --petal-yellow: #f6dd83;
    --leaf: #8fc4a4;
  }
  * { margin: 0; padding: 0; box-sizing: border-box; }
  html, body { width: 973px; height: 1200px; overflow: hidden; background: #e9e9e9; }
  .flyer {
    position: relative;
    width: 973px;
    height: 1200px;
    overflow: hidden;
    background: radial-gradient(ellipse 70% 45% at 50% 18%, var(--plum-light) 0%, var(--plum-mid) 55%, var(--plum-deep) 100%);
    text-align: center;
    color: var(--white);
  }
  .floral-band {
    position: absolute;
    left: 0;
    width: 973px;
  }
  .floral-band--top {
    top: 0;
    height: 200px;
    background: linear-gradient(90deg, var(--petal-pink), var(--petal-rose) 22%, var(--petal-yellow) 38%, var(--petal-pink) 52%, var(--petal-rose) 70%, var(--petal-pink) 88%, var(--petal-yellow));
    -webkit-mask: linear-gradient(180deg, #000 55%, transparent 100%);
            mask: linear-gradient(180deg, #000 55%, transparent 100%);
  }
  .floral-band--bottom {
    bottom: 0;
    height: 210px;
    background: linear-gradient(90deg, var(--petal-pink), var(--petal-rose) 18%, var(--petal-yellow) 34%, var(--petal-pink) 48%, var(--petal-rose) 64%, var(--petal-yellow) 78%, var(--petal-pink));
    -webkit-mask: linear-gradient(0deg, #000 60%, transparent 100%);
            mask: linear-gradient(0deg, #000 60%, transparent 100%);
  }
  .accent {
    position: absolute;
    border-radius: 50%;
  }
  .accent--butterfly-left { left: 28px; top: 225px; width: 60px; height: 44px; background: #b98a4e; opacity: .8; }
  .accent--butterfly-right { right: 95px; top: 248px; width: 50px; height: 46px; background: var(--petal-pink); opacity: .85; }
  .accent--sprig-left { left: 0; top: 190px; width: 50px; height: 170px; background: linear-gradient(180deg, var(--leaf), transparent); opacity: .6; }
  .accent--bloom-left { left: 38px; top: 840px; width: 64px; height: 64px; background: var(--petal-yellow); opacity: .9; }
  .accent--bloom-right { right: 42px; top: 875px; width: 64px; height: 64px; background: var(--petal-yellow); opacity: .9; }
  .accent--butterfly-low { left: 42px; top: 915px; width: 66px; height: 46px; background: #b98a4e; opacity: .8; }

  .presenter {
    position: absolute;
    top: 195px;
    left: 0;
    width: 100%;
    font-family: "Cormorant Garamond", serif;
    font-weight: 500;
    font-size: 40px;
    color: var(--white);
    letter-spacing: .5px;
  }
  .show-title {
    position: absolute;
    top: 290px;
    left: 0;
    width: 100%;
    font-family: "Kaushan Script", cursive;
    font-size: 112px;
    line-height: 1.1;
    background: linear-gradient(180deg, var(--gold-light), var(--gold));
    -webkit-background-clip: text;
            background-clip: text;
    color: transparent;
  }
  .show-subtitle {
    position: absolute;
    top: 455px;
    left: 0;
    width: 100%;
    font-family: "Archivo", sans-serif;
    font-weight: 800;
    font-size: 62px;
    letter-spacing: 3px;
    color: var(--cream);
  }
  .schedule {
    position: absolute;
    top: 548px;
    left: 50%;
    width: 310px;
    transform: translateX(-50%);
    font-family: "Cormorant Garamond", serif;
  }
  .schedule__date { font-size: 23px; font-weight: 500; letter-spacing: 1px; padding-bottom: 6px; border-bottom: 1px solid var(--rule); }
  .schedule__time { font-size: 21px; font-weight: 700; letter-spacing: 1px; padding: 7px 0 8px; border-bottom: 1px solid var(--rule); }
  .venue {
    position: absolute;
    top: 640px;
    left: 0;
    width: 100%;
    font-family: "Cormorant Garamond", serif;
  }
  .venue__name { font-size: 29px; font-weight: 500; letter-spacing: 1px; }
  .venue__address { font-size: 20px; font-weight: 500; margin-top: 4px; }
  .guests-banner {
    position: absolute;
    top: 712px;
    left: 50%;
    transform: translateX(-50%);
    width: 480px;
    height: 50px;
  }
  .guests-banner svg { position: absolute; inset: 0; }
  .guests-banner__label {
    position: relative;
    font-family: "Cormorant Garamond", serif;
    font-weight: 700;
    font-size: 29px;
    line-height: 50px;
    letter-spacing: 1px;
    color: var(--white);
  }
  .guest-list {
    position: absolute;
    top: 778px;
    left: 0;
    width: 100%;
    list-style: none;
    font-family: "Kaushan Script", cursive;
    font-size: 32px;
    line-height: 47px;
    color: var(--gold);
  }
  .tickets {
    position: absolute;
    top: 932px;
    left: 0;
    width: 100%;
    font-family: "Archivo", sans-serif;
    font-weight: 700;
  }
  .tickets__heading { font-size: 22px; letter-spacing: .5px; }
  .tickets__prices { font-size: 18px; margin-top: 2px; }
  .tickets__dot { color: var(--petal-pink); margin: 0 6px; }
</style>
</head>
<body>
<main class="flyer">
  <div class="floral-band floral-band--top" role="img" aria-label="Watercolour border of pink, rose and yellow flowers with green leaves"></div>
  <div class="accent accent--sprig-left" role="img" aria-label="Green leafy sprig with yellow berries"></div>
  <div class="accent accent--butterfly-left" role="img" aria-label="Orange butterfly illustration"></div>
  <div class="accent accent--butterfly-right" role="img" aria-label="Pink butterfly illustration"></div>

  <p class="presenter">Harmonies of the Coast</p>
  <h1 class="show-title">Maple Chorus</h1>
  <h2 class="show-subtitle">REVUE</h2>

  <div class="schedule">
    <p class="schedule__date">FRIDAY, APRIL 8, 2022</p>
    <p class="schedule__time">2 P.M. &amp; 7 P.M.</p>
  </div>

  <div class="venue">
    <p class="venue__name">LARKWOOD HIGH SCHOOL</p>
    <p class="venue__address">4286 Fernhollow Rd, Citrus Heights, CA 95617</p>
  </div>

  <div class="guests-banner">
    <svg width="480" height="50" viewBox="0 0 480 50" aria-hidden="true">
      <polygon points="0,0 480,0 462,25 480,50 0,50 18,25" fill="var(--sage)"/>
    </svg>
    <p class="guests-banner__label">SPECIAL GUESTS:</p>
  </div>

  <ul class="guest-list">
    <li>Bright Chord</li>
    <li>Harbor Quartet</li>
    <li>Copperleaf Five</li>
  </ul>

  <div class="tickets">
    <p class="tickets__heading">TICKET PRICES:</p>
    <p class="tickets__prices">VIP $35.00 <span class="tickets__dot">•</span>General $25.00<span class="tickets__dot">•</span>Student $15.00</p>
  </div>

  <div class="accent accent--bloom-left" role="img" aria-label="Small yellow flower"></div>
  <div class="accent accent--bloom-right" role="img" aria-label="Small yellow flower"></div>
  <div class="accent accent--butterfly-low" role="img" aria-label="Orange butterfly illustration"></div>
  <div class="floral-band floral-band--bottom" role="img" aria-label="Watercolour border of pink, rose and yellow flowers with green leaves and berries"></div>
</main>
</body>
</html>
```